We want our 2017 Olvane Stride Hauler 340 Van Medium Roof 148 WB to POP

We are a lawn and property management company that specializes in lawn care; mowing, fertilizing, weed control, seasonal clean up, and full Property Management; interior and exterior cleaning, maintenence , and more.
Our vans are white and we do not want to full body wraps. Just strategically placed decals.
Simple, minimalist design without a lot of fuss or detail.

Target Market(s)

Local community members. Residential and Commercial

Industry/Entity Type

Lawn and Property Management

Requirements
Must have
• Phone number: 608-555-0193 website: www.quarrybrookyard.com
Should not have
• Cartoon characters or loud, obnoxious graphics

```html
<!DOCTYPE html>
<html lang="en">
<head>
<meta charset="utf-8">
<title>QuarryBrook Lawn and Property Management – Van Decals</title>
<link rel="stylesheet" href="https://fonts.googleapis.com/css2?family=Montserrat:wght@600;700&family=Barlow:wght@500;600&display=swap">
<style>
  :root {
    --green: #3f9a2b;
    --green-dark: #2f7f1f;
    --purple: #6a1b9a;
    --ink: #141414;
    --panel: #ffffff;
    --stage: #eef0f2;
    --rule: #5aa845;
  }
  * { box-sizing: border-box; margin: 0; padding: 0; }
  html, body { width: 1200px; height: 800px; overflow: hidden; background: var(--stage); }
  body { position: relative; font-family: "Barlow", Arial, sans-serif; color: var(--ink); }

  .decal-panel { position: absolute; background: var(--panel); border-radius: 10px; overflow: hidden; }
  .side-panel { left: 20px; top: 20px; width: 1160px; height: 450px; }
  .hood-panel { left: 20px; top: 490px; width: 500px; height: 290px; }
  .rear-panel { left: 540px; top: 490px; width: 640px; height: 290px; }

  .brand { position: absolute; display: flex; align-items: center; gap: 14px; }
  .brand-dot { border-radius: 50%; border: 4px solid var(--green); flex: none; }
  .brand-name { font-family: "Montserrat", Arial, sans-serif; font-weight: 700; color: var(--ink); line-height: 1; letter-spacing: -1px; white-space: nowrap; }
  .brand-tag { font-family: "Montserrat", Arial, sans-serif; font-weight: 600; letter-spacing: 1.2px; color: var(--ink); text-transform: uppercase; white-space: nowrap; }

  .services { position: absolute; list-style: none; }
  .service { display: flex; align-items: center; gap: 10px; font-weight: 600; text-transform: uppercase; border-bottom: 1.5px solid var(--rule); white-space: nowrap; }
  .service.is-highlight { color: var(--purple); border-bottom: none; }
  .service-icon { border-radius: 50%; background: var(--green); display: flex; align-items: center; justify-content: center; flex: none; }
  .service-icon svg { width: 60%; height: 60%; }
  .service.is-highlight .service-icon { background: var(--purple); }
  .services-note { font-weight: 600; text-transform: uppercase; margin-top: 4px; white-space: nowrap; }

  .contact { position: absolute; }
  .contact-phone { display: flex; align-items: center; gap: 8px; font-weight: 600; color: var(--purple); line-height: 1; white-space: nowrap; }
  .contact-web { display: flex; align-items: center; gap: 8px; font-weight: 600; color: var(--green-dark); line-height: 1; white-space: nowrap; }

  .swoosh { position: absolute; }

  /* side */
  .side-panel .brand { left: 330px; top: 90px; }
  .side-panel .brand-dot { width: 100px; height: 100px; }
  .side-panel .brand-name { font-size: 40px; }
  .side-panel .brand-tag { font-size: 11px; margin-top: 7px; }
  .side-panel .services { left: 820px; top: 42px; width: 260px; }
  .side-panel .service { font-size: 17px; height: 36px; }
  .side-panel .service-icon { width: 29px; height: 29px; }
  .side-panel .services-note { font-size: 14px; }
  .side-panel .contact { left: 150px; top: 258px; }
  .side-panel .contact-phone { font-size: 27px; }
  .side-panel .contact-web { font-size: 15px; margin-top: 10px; }
  .side-panel .swoosh { left: 380px; top: 240px; width: 440px; height: 80px; }

  /* hood */
  .hood-panel .swoosh { left: 0; top: 0; width: 500px; height: 290px; }
  .hood-panel .brand { left: 0; right: 0; top: 110px; justify-content: center; }
  .hood-panel .brand-dot { width: 30px; height: 30px; border-width: 3px; }
  .hood-panel .brand-name { font-size: 30px; }
  .hood-panel .brand-tag { font-size: 8.5px; margin-top: 3px; }

  /* rear */
  .rear-panel .brand { left: 40px; top: 24px; flex-direction: column; align-items: center; gap: 8px; }
  .rear-panel .brand-dot { width: 56px; height: 56px; }
  .rear-panel .brand-name { font-size: 34px; text-align: center; }
  .rear-panel .brand-tag { font-size: 9px; margin-top: 4px; text-align: center; }
  .rear-panel .services { left: 345px; top: 12px; width: 240px; }
  .rear-panel .service { font-size: 12.5px; height: 22px; gap: 8px; }
  .rear-panel .service-icon { width: 18px; height: 18px; }
  .rear-panel .services-note { font-size: 10px; }
  .rear-panel .swoosh { left: 0; top: 140px; width: 640px; height: 150px; }
  .rear-panel .contact { left: 40px; top: 206px; }
  .rear-panel .contact-phone { font-size: 32px; }
  .rear-panel .contact-web { font-size: 19px; margin-top: 10px; }
</style>
</head>
<body>

<section class="decal-panel side-panel" aria-label="Side decal">
  <svg class="swoosh" viewBox="0 0 440 80" preserveAspectRatio="none" aria-hidden="true">
    <path d="M0 80 L440 0 L440 16 L110 80 Z" fill="var(--green)"/>
    <path d="M300 80 L440 22 L440 36 L340 80 Z" fill="var(--purple)"/>
  </svg>

  <div class="brand">
    <span class="brand-dot"></span>
    <div>
      <div class="brand-name">QuarryBrook</div>
      <div class="brand-tag">Lawn and Property Management</div>
    </div>
  </div>

  <ul class="services">
    <li class="service"><span class="service-icon"><svg viewBox="0 0 20 20"><path d="M3 15 L5 7 L8 12 L10 5 L12 12 L15 7 L17 15 Z" fill="#fff"/></svg></span>Lawn Care</li>
    <li class="service"><span class="service-icon"><svg viewBox="0 0 20 20"><rect x="4" y="8" width="10" height="5" fill="#fff"/><line x1="14" y1="8" x2="17" y2="3" stroke="#fff" stroke-width="1.6"/><circle cx="6" cy="15" r="2" fill="#fff"/><circle cx="13" cy="15" r="2" fill="#fff"/></svg></span>Mowing</li>
    <li class="service"><span class="service-icon"><svg viewBox="0 0 20 20"><path d="M4 16 C4 8 9 4 16 4 C16 11 12 16 4 16 Z" fill="#fff"/></svg></span>Fertilizing</li>
    <li class="service"><span class="service-icon"><svg viewBox="0 0 20 20"><path d="M10 17 V6 M10 10 C7 10 5 8 5 5 C8 5 10 7 10 10 M10 10 C13 10 15 8 15 5 C12 5 10 7 10 10" stroke="#fff" stroke-width="1.6" fill="none"/></svg></span>Weed Control</li>
    <li class="service"><span class="service-icon"><svg viewBox="0 0 20 20"><path d="M4 16 C4 8 9 4 16 4 C16 11 12 16 4 16 Z" fill="#fff"/></svg></span>Seasonal Clean Up</li>
    <li class="service is-highlight"><span class="service-icon"><svg viewBox="0 0 20 20"><path d="M3 10 L10 4 L17 10 H15 V16 H5 V10 Z" fill="#fff"/></svg></span>Property Management</li>
    <li class="services-note">Cleaning, Maintenance and More</li>
  </ul>

  <div class="contact">
    <div class="contact-phone">
      <svg width="22" height="22" viewBox="0 0 24 24"><path d="M6.6 10.8a15 15 0 0 0 6.6 6.6l2.2-2.2c.3-.3.7-.4 1-.2 1.1.4 2.3.6 3.6.6.6 0 1 .4 1 1V20c0 .6-.4 1-1 1A17 17 0 0 1 3 4c0-.6.4-1 1-1h3.5c.6 0 1 .4 1 1 0 1.3.2 2.5.6 3.6.1.3 0 .7-.2 1z" fill="currentColor"/></svg>
      608-555-0193
    </div>
    <div class="contact-web">
      <svg width="18" height="18" viewBox="0 0 20 20"><circle cx="10" cy="10" r="8" fill="none" stroke="currentColor" stroke-width="1.8"/><path d="M2 10 H18 M10 2 C6 6 6 14 10 18 M10 2 C14 6 14 14 10 18" stroke="currentColor" stroke-width="1.4" fill="none"/></svg>
      www.quarrybrookyard.com
    </div>
  </div>
</section>

<section class="decal-panel hood-panel" aria-label="Hood decal">
  <svg class="swoosh" viewBox="0 0 500 290" aria-hidden="true">
    <path d="M70 120 C100 125 120 140 130 160" stroke="var(--purple)" stroke-width="5" fill="none"/>
    <path d="M430 120 C400 125 380 140 370 160" stroke="var(--purple)" stroke-width="5" fill="none"/>
    <path d="M440 110 C410 112 388 124 376 140" stroke="var(--green)" stroke-width="4" fill="none"/>
  </svg>
  <div class="brand">
    <span class="brand-dot"></span>
    <div>
      <div class="brand-name">QuarryBrook</div>
      <div class="brand-tag">Lawn and Property Management</div>
    </div>
  </div>
</section>

<section class="decal-panel rear-panel" aria-label="Rear doors decal">
  <svg class="swoosh" viewBox="0 0 640 150" preserveAspectRatio="none" aria-hidden="true">
    <path d="M0 14 C200 2 420 22 640 46 L640 62 C420 38 200 20 0 28 Z" fill="var(--green)"/>
    <path d="M0 34 C220 20 420 42 600 150 L570 150 C410 60 220 38 0 46 Z" fill="var(--purple)"/>
  </svg>

  <div class="brand">
    <span class="brand-dot"></span>
    <div>
      <div class="brand-name">QuarryBrook</div>
      <div class="brand-tag">Lawn and Property Management</div>
    </div>
  </div>

  <ul class="services">
    <li class="service"><span class="service-icon"><svg viewBox="0 0 20 20"><path d="M3 15 L5 7 L8 12 L10 5 L12 12 L15 7 L17 15 Z" fill="#fff"/></svg></span>Lawn Care</li>
    <li class="service"><span class="service-icon"><svg viewBox="0 0 20 20"><rect x="4" y="8" width="10" height="5" fill="#fff"/><circle cx="6" cy="15" r="2" fill="#fff"/><circle cx="13" cy="15" r="2" fill="#fff"/></svg></span>Mowing</li>
    <li class="service"><span class="service-icon"><svg viewBox="0 0 20 20"><path d="M4 16 C4 8 9 4 16 4 C16 11 12 16 4 16 Z" fill="#fff"/></svg></span>Fertilizing</li>
    <li class="service"><span class="service-icon"><svg viewBox="0 0 20 20"><path d="M10 17 V6 M10 10 C7 10 5 8 5 5 C8 5 10 7 10 10 M10 10 C13 10 15 8 15 5 C12 5 10 7 10 10" stroke="#fff" stroke-width="1.6" fill="none"/></svg></span>Weed Control</li>
    <li class="service"><span class="service-icon"><svg viewBox="0 0 20 20"><path d="M4 16 C4 8 9 4 16 4 C16 11 12 16 4 16 Z" fill="#fff"/></svg></span>Seasonal Clean Up</li>
    <li class="service is-highlight"><span class="service-icon"><svg viewBox="0 0 20 20"><path d="M3 10 L10 4 L17 10 H15 V16 H5 V10 Z" fill="#fff"/></svg></span>Property Management</li>
    <li class="services-note">Cleaning, Maintenance and More</li>
  </ul>

  <div class="contact">
    <div class="contact-phone">
      <svg width="26" height="26" viewBox="0 0 24 24"><path d="M6.6 10.8a15 15 0 0 0 6.6 6.6l2.2-2.2c.3-.3.7-.4 1-.2 1.1.4 2.3.6 3.6.6.6 0 1 .4 1 1V20c0 .6-.4 1-1 1A17 17 0 0 1 3 4c0-.6.4-1 1-1h3.5c.6 0 1 .4 1 1 0 1.3.2 2.5.6 3.6.1.3 0 .7-.2 1z" fill="currentColor"/></svg>
      608-555-0193
    </div>
    <div class="contact-web">
      <svg width="22" height="22" viewBox="0 0 20 20"><circle cx="10" cy="10" r="8" fill="none" stroke="currentColor" stroke-width="1.8"/><path d="M2 10 H18 M10 2 C6 6 6 14 10 18 M10 2 C14 6 14 14 10 18" stroke="currentColor" stroke-width="1.4" fill="none"/></svg>
      www.quarrybrookyard.com
    </div>
  </div>
</section>

</body>
</html>
```